80's style coming soon instagram post

I would like the black and white photo to be created into an 80's style poster like the 'glint' attachment with the text to read 'coming soon'.

```html
<!DOCTYPE html>
<html lang="en">
<head>
<meta charset="utf-8">
<title>Coming Soon — Retro Poster</title>
<link rel="stylesheet" href="https://fonts.googleapis.com/css2?family=Mr+Dafoe&display=swap">
<style>
  :root {
    --night: #0d1f26;
    --night-deep: #081418;
    --neon-pink: #e0307a;
    --hot-magenta: #ff2fa8;
    --soft-lilac: #c58fd8;
    --aqua: #63e6e2;
    --aqua-deep: #2fb8b8;
  }
  html, body {
    margin: 0;
    padding: 0;
    overflow: hidden;
    background: var(--night-deep);
  }
  .poster {
    position: relative;
    width: 945px;
    height: 1200px;
    overflow: hidden;
    background: radial-gradient(ellipse at 50% 45%, #12303a 0%, var(--night) 55%, var(--night-deep) 100%);
  }
  .poster-art {
    position: absolute;
    inset: 0;
    width: 945px;
    height: 1200px;
  }
  .headline {
    position: absolute;
    left: 0;
    right: 0;
    top: 930px;
    margin: 0;
    text-align: center;
    font-family: "Mr Dafoe", cursive;
    font-weight: 400;
    font-size: 190px;
    line-height: 1;
    letter-spacing: 2px;
    background: linear-gradient(180deg, var(--aqua) 0%, var(--aqua) 38%, var(--soft-lilac) 55%, var(--hot-magenta) 80%, var(--neon-pink) 100%);
    -webkit-background-clip: text;
    background-clip: text;
    color: transparent;
    transform: rotate(-3deg);
  }
</style>
</head>
<body>
  <main class="poster">
    <svg class="poster-art" viewBox="0 0 945 1200" xmlns="http://www.w3.org/2000/svg">
      <defs>
        <linearGradient id="stripe-fade" x1="0" y1="0" x2="0" y2="1">
          <stop offset="0" stop-color="#d63572"/>
          <stop offset="0.25" stop-color="#d64f8a"/>
          <stop offset="0.42" stop-color="#c8a9d6"/>
          <stop offset="0.6" stop-color="#7fd8d8"/>
          <stop offset="1" stop-color="#2fa7aa"/>
        </linearGradient>
        <pattern id="stripe-lines" width="945" height="40" patternUnits="userSpaceOnUse" y="22">
          <rect x="0" y="0" width="945" height="24" fill="#fff"/>
        </pattern>
        <mask id="stripe-mask">
          <rect x="34" y="22" width="890" height="770" fill="url(#stripe-lines)"/>
        </mask>
        <linearGradient id="sunset-disc" x1="0" y1="0" x2="0" y2="1">
          <stop offset="0" stop-color="#2fb8c4"/>
          <stop offset="0.45" stop-color="#8a6fc8"/>
          <stop offset="0.75" stop-color="#e0307a"/>
          <stop offset="1" stop-color="#3a1a3a"/>
        </linearGradient>
        <radialGradient id="portrait-tone" cx="0.5" cy="0.45" r="0.6">
          <stop offset="0" stop-color="#6fe3df"/>
          <stop offset="0.6" stop-color="#3fb3b3"/>
          <stop offset="1" stop-color="#123038"/>
        </radialGradient>
        <linearGradient id="portrait-fade" x1="0" y1="0" x2="0" y2="1">
          <stop offset="0.75" stop-color="#fff"/>
          <stop offset="1" stop-color="#000"/>
        </linearGradient>
        <mask id="portrait-mask">
          <rect x="0" y="0" width="945" height="1200" fill="url(#portrait-fade)"/>
        </mask>
      </defs>

      <rect class="stripe-band" x="34" y="22" width="890" height="770" fill="url(#stripe-fade)" mask="url(#stripe-mask)"/>

      <circle class="sunset-disc" cx="477" cy="610" r="369" fill="url(#sunset-disc)" role="img" aria-label="Sunset disc with palm tree silhouettes and a retro car"/>

      <g mask="url(#portrait-mask)">
        <path class="portrait" role="img" aria-label="Portrait of a smiling bearded man in sunglasses, duotone aqua and magenta"
              d="M210 120 Q300 20 480 30 Q690 40 760 200 L790 520 Q860 700 864 900 L180 900 Q170 700 200 560 Q130 420 150 360 Q170 200 210 120 Z"
              fill="url(#portrait-tone)"/>
      </g>
    </svg>

    <h1 class="headline">Coming Soon</h1>
  </main>
</body>
</html>
```